I need the below text put into an illustration/high res image so I can print out and frame and give to my fiance. Can be simple but must look elegant. Idea is that the text can be written in the sand on the attached pics (let me know if you require more high res). Not precious on the dimensions but think no more than 90cm length or width. Can be smaller whatever you think works best. You can half long sentences if you think it will look better.
Update: some of you asked for a picture of us, not sure it works but have attached one
Marriage
Marriage isn’t for you.
You don’t marry to make yourself happy, you marry to make someone else happy.
More than that, your marriage isn’t for yourself, you’re marrying for a family.
Not just for the in-laws and all of that nonsense, but for your future children.
Who do you want to help you raise them?
Who do you want to influence them?
Marriage isn’t for you.
It’s not about you.
Marriage is about the person you married.

```html
<!DOCTYPE html>
<html lang="en">
<head>
<meta charset="utf-8">
<title>Marriage</title>
<link rel="stylesheet" href="https://fonts.googleapis.com/css2?family=Rochester&family=Tinos&display=swap">
<style>
  :root {
    --sky-top: #c9dcec;
    --sky-low: #eef3f6;
    --sea-deep: #4f7f9e;
    --sea-foam: #bcd3df;
    --wet-sand: #a9c3d2;
    --sand-light: #b9b6ad;
    --sand-dark: #8f8b83;
    --haze: rgba(235, 235, 232, 0.75);
    --portrait-cool: #3f5a7a;
    --portrait-mid: #5a6a62;
    --portrait-olive: #6d6a3a;
    --portrait-sky: #4a8cb8;
    --title-fill: #56656a;
    --title-edge: #1f2a2e;
    --verse-ink: #232323;
    --verse-glow: #ffffff;
  }
  html, body {
    margin: 0;
    padding: 0;
    overflow: hidden;
    background: #ffffff;
  }
  .canvas {
    position: relative;
    width: 1200px;
    height: 900px;
    overflow: hidden;
  }
  .beach-scene {
    position: absolute;
    inset: 0;
    background:
      radial-gradient(ellipse 340px 360px at 880px 470px, var(--haze), rgba(235,235,232,0) 70%),
      linear-gradient(160deg, rgba(169,195,210,0.85) 0%, rgba(169,195,210,0.6) 28%, rgba(169,195,210,0) 45%),
      linear-gradient(180deg,
        var(--sky-top) 0px,
        var(--sky-low) 55px,
        var(--sea-deep) 70px,
        var(--sea-foam) 110px,
        var(--wet-sand) 140px,
        var(--sand-light) 260px,
        var(--sand-dark) 900px);
  }
  .couple-portrait {
    position: absolute;
    left: 0;
    top: 285px;
    width: 720px;
    height: 615px;
    border-top-right-radius: 260px 300px;
    background: linear-gradient(120deg,
      var(--portrait-cool) 0%,
      var(--portrait-mid) 35%,
      var(--portrait-olive) 60%,
      var(--portrait-sky) 100%);
    opacity: 0.95;
  }
  .poem-title {
    position: absolute;
    left: 630px;
    top: 138px;
    margin: 0;
    font-family: "Rochester", cursive;
    font-weight: 400;
    font-size: 96px;
    line-height: 100px;
    color: var(--title-fill);
    -webkit-text-stroke: 1.5px var(--title-edge);
    text-shadow: 1px 2px 2px rgba(0,0,0,0.45), -1px -1px 1px rgba(255,255,255,0.6);
  }
  .poem-verses {
    position: absolute;
    left: 580px;
    top: 264px;
    width: 600px;
    text-align: center;
  }
  .verse {
    margin: 0;
    font-family: "Tinos", "Times New Roman", serif;
    font-size: 25.5px;
    line-height: 25px;
    color: var(--verse-ink);
    text-shadow: 0 0 4px var(--verse-glow), 0 0 8px var(--verse-glow);
  }
  .verse + .verse { margin-top: 21px; }
</style>
</head>
<body>
<main class="canvas">
  <div class="beach-scene" role="img" aria-label="Beach at the water's edge with waves, a headland and pine trees under a pale sky"></div>
  <div class="couple-portrait" role="img" aria-label="Selfie photo of the couple together on the beach"></div>

  <section class="poem">
    <h1 class="poem-title">Marriage</h1>
    <div class="poem-verses">
      <p class="verse">Marriage isn’t for you.</p>
      <p class="verse">You don’t marry to make yourself happy,<br>you marry to make someone else happy.</p>
      <p class="verse">More than that, your marriage isn’t for yourself,<br>you’re marrying for a family.</p>
      <p class="verse">Not just for the in-laws and all of that nonsense,<br>but for your future children.</p>
      <p class="verse">Who do you want to help you raise them?</p>
      <p class="verse">Who do you want to influence them?</p>
      <p class="verse">Marriage isn’t for you.</p>
      <p class="verse">It’s not about you.</p>
      <p class="verse">Marriage is about the person you married.</p>
    </div>
  </section>
</main>
</body>
</html>
```